Structural Engineering Company needs ad for magazine

We are an engineering office for structural engineering in the entertainment industry. Our focus are concert stages, festival structures, grand stands and exhibition booths. Our customers are mainly from Europe, we realize the projects worldwide. Typical customers are designer, architects, stage builders, exhibition builder and technical service provider. We are creating structural analyses, technical consulting, technical drawings and risk assessment. We are working on mid size and major events.
Some technical notes:
- CMYK profile needed, minimum 300 dpi for raster graphic
- Our primary color is Petrol. Favourite is petrol, coral and grey (black). Please use palette shown below.
- Our font in documents is Myriad. Regular at 10 pt for text and Light at 16-24pt for titles.
- The format for the ad is 61 x 127 mm (portrait) or 185 x 46 mm (landscape). Which one is up to you.
To the content:
- For contact details we just want to provide our web address "belsokar.de" and/or our e-mail "info@belsokar.de"
- Attached are some Logo files and photos.
- The ad do not advertise a specific product. It is more a general advertisement for the company.
- The language for the ad should be German. Below are keywords in English and corresponding German translation. You do not need to place all Keywords, it is just a brainstorming list to help you. You are also welcome to use other text. We will help with translation, if necessary.
- we like discussing ideas to get better results, so also if you have questions, please ask.
- If you need information that we haven't thought of yet, please ask.
Our slogan (also in Germany): event meets engineering
Service Keywords EN / DE
- Structural Analysis / Statische Berechnungen
- Risk Assessment / Risikobewertungen
- Consulting & Design / Beratung & Konstruktion
Technical Keywords EN / DE
- Stage machinery / Bühnentechnik
- Scaffolding / Gerüstbau
- Exhibition Booths / Messebauten
- Tents / Zelte
- Temporary Structures / Fliegende Bauten
- Truss / Traversen
- Stages / Bühnen
- Grand Stands / Tribünen
- Leightweight Construction / Leichtbau
- Steel Construction / Stahlbau
- Amusement Rides / Fahrgeschäfte
Look and feel
Each slider illustrates characteristics of the customer's brand and the style your logo design should communicate.

```html
<!DOCTYPE html>
<html lang="de">
<head>
<meta charset="utf-8">
<title>Belsokar Engineering – Event meets Engineering</title>
<link href="https://fonts.googleapis.com/css2?family=Montserrat:wght@400;500;700&display=swap" rel="stylesheet">
<style>
  :root {
    --petrol: #2bb5cf;
    --ink: #232123;
    --white: #ffffff;
    --page: #8a8a8a;
  }
  * { margin: 0; padding: 0; box-sizing: border-box; }
  html, body { width: 1200px; height: 1054px; overflow: hidden; background: var(--page); }
  body { font-family: "Montserrat", sans-serif; color: var(--white); }

  .flyer {
    position: absolute; left: 358px; top: 27px;
    width: 484px; height: 1000px;
    background: var(--ink); overflow: hidden;
  }
  .hero-photo {
    position: absolute; left: 0; top: 0; width: 484px; height: 430px;
    background: linear-gradient(180deg, #9aa3ab 0%, #5f6c78 30%, #2f6e9a 55%, #3fa9c4 70%, #c9c9c5 85%, #dcdcd8 100%);
    clip-path: polygon(0 0, 100% 0, 100% 291px, 0 418px);
  }
  .hero-band { position: absolute; left: 0; top: 0; width: 484px; height: 430px; }

  .brand-seal {
    position: absolute; left: 41px; top: 277px; width: 174px; height: 174px;
    border-radius: 50%; background: var(--petrol);
    display: flex; align-items: center; justify-content: center; text-align: center;
  }
  .brand-name {
    font-weight: 500; font-size: 15px; letter-spacing: 2.5px; line-height: 1.35; color: var(--white);
  }

  .slogan {
    position: absolute; left: 0; top: 458px; width: 484px; text-align: center;
    font-weight: 700; font-size: 26.5px; color: var(--petrol); letter-spacing: 0.2px;
  }

  .services { position: absolute; left: 0; top: 505px; width: 484px; height: 100px; }
  .service-label {
    position: absolute; top: 577px; width: 130px; text-align: center;
    font-size: 13px; line-height: 1.1; color: var(--white);
  }

  .keywords {
    position: absolute; top: 640px; list-style: none;
    font-size: 18px; line-height: 25.3px;
  }
  .keywords li { display: flex; align-items: center; gap: 11px; }
  .keywords svg { width: 14px; height: 14px; flex: none; }
  .keywords.left { left: 44px; }
  .keywords.right { left: 267px; }

  .gallery { position: absolute; top: 816px; left: 25px; display: flex; gap: 6px; }
  .gallery-photo { width: 148px; height: 117px; }
  .gallery-photo.stage { background: linear-gradient(135deg, #8d9399, #d7dadc 50%, #5f7e94); }
  .gallery-photo.light { background: linear-gradient(160deg, #9aa0c4, #6d3fd0 45%, #c04fd6 75%, #2a1b5c); }
  .gallery-photo.outdoor { background: linear-gradient(180deg, #dfe6ec 0%, #c5cfd3 40%, #6e7a55 65%, #a9a79a 100%); }

  .contact-bar {
    position: absolute; left: 28px; top: 952px; width: 452px; height: 48px;
    background: var(--petrol); border-radius: 22px 22px 0 0;
    display: flex; align-items: center; justify-content: center; gap: 18px;
    font-size: 18px; color: var(--white);
  }
  .contact-bar span { display: flex; align-items: center; gap: 5px; }
  .contact-bar svg { width: 14px; height: 14px; }
</style>
</head>
<body>
<main class="flyer">
  <div class="hero-photo" role="img" aria-label="Foto: Bühnenaufbau mit Traversen und Kran in einem Stadion"></div>
  <svg class="hero-band" viewBox="0 0 484 430" aria-hidden="true">
    <polygon points="0,418 484,291 484,340 0,470" fill="var(--petrol)"/>
    <polygon points="0,440 484,325 484,430 0,430" fill="var(--ink)"/>
  </svg>

  <div class="brand-seal"><p class="brand-name">BELSOKAR<br>ENGINEERING</p></div>

  <h1 class="slogan">EVENT MEETS ENGINEERING</h1>

  <svg class="services" viewBox="0 0 484 100" aria-hidden="true">
    <g stroke="var(--white)" stroke-width="1.3" stroke-dasharray="2 4" fill="none">
      <line x1="124" y1="38" x2="212" y2="38"/>
      <line x1="287" y1="36" x2="373" y2="36"/>
    </g>
    <g fill="var(--petrol)" stroke="var(--white)" stroke-width="2">
      <circle cx="86" cy="38" r="34"/>
      <circle cx="249" cy="36" r="34"/>
      <circle cx="410" cy="34" r="34"/>
    </g>
    <g fill="none" stroke="var(--white)" stroke-width="2" stroke-linecap="round" stroke-linejoin="round">
      <path d="M72 34 a14 14 0 0 1 28 0 z M68 34 h36 M86 20 v8"/>
      <path d="M70 60 q16 -14 32 0"/>
      <circle cx="245" cy="32" r="12"/>
      <line x1="254" y1="41" x2="264" y2="51"/>
      <circle cx="410" cy="34" r="14"/>
      <circle cx="410" cy="34" r="5"/>
      <path d="M393 34 h34"/>
    </g>
  </svg>
  <p class="service-label" style="left:21px">Statische<br>Berechnungen</p>
  <p class="service-label" style="left:175px;width:148px">Risikobewertungen</p>
  <p class="service-label" style="left:345px">Beratung &amp;<br>Konstruktion</p>

  <ul class="keywords left">
    <li><svg viewBox="0 0 14 14"><circle cx="7" cy="7" r="6" fill="none" stroke="#fff" stroke-width="1.3"/><path d="M6 4l3 3-3 3" fill="none" stroke="#fff" stroke-width="1.5"/></svg>Bühnentechnik</li>
    <li><svg viewBox="0 0 14 14"><circle cx="7" cy="7" r="6" fill="none" stroke="#fff" stroke-width="1.3"/><path d="M6 4l3 3-3 3" fill="none" stroke="#fff" stroke-width="1.5"/></svg>Gerüstbau</li>
    <li><svg viewBox="0 0 14 14"><circle cx="7" cy="7" r="6" fill="none" stroke="#fff" stroke-width="1.3"/><path d="M6 4l3 3-3 3" fill="none" stroke="#fff" stroke-width="1.5"/></svg>Messebauten</li>
    <li><svg viewBox="0 0 14 14"><circle cx="7" cy="7" r="6" fill="none" stroke="#fff" stroke-width="1.3"/><path d="M6 4l3 3-3 3" fill="none" stroke="#fff" stroke-width="1.5"/></svg>Zelte</li>
    <li><svg viewBox="0 0 14 14"><circle cx="7" cy="7" r="6" fill="none" stroke="#fff" stroke-width="1.3"/><path d="M6 4l3 3-3 3" fill="none" stroke="#fff" stroke-width="1.5"/></svg>Fliegende Bauten</li>
    <li><svg viewBox="0 0 14 14"><circle cx="7" cy="7" r="6" fill="none" stroke="#fff" stroke-width="1.3"/><path d="M6 4l3 3-3 3" fill="none" stroke="#fff" stroke-width="1.5"/></svg>Traversen</li>
  </ul>
  <ul class="keywords right">
    <li><svg viewBox="0 0 14 14"><circle cx="7" cy="7" r="6" fill="none" stroke="#fff" stroke-width="1.3"/><path d="M6 4l3 3-3 3" fill="none" stroke="#fff" stroke-width="1.5"/></svg>Bühnen</li>
    <li><svg viewBox="0 0 14 14"><circle cx="7" cy="7" r="6" fill="none" stroke="#fff" stroke-width="1.3"/><path d="M6 4l3 3-3 3" fill="none" stroke="#fff" stroke-width="1.5"/></svg>Tribünen</li>
    <li><svg viewBox="0 0 14 14"><circle cx="7" cy="7" r="6" fill="none" stroke="#fff" stroke-width="1.3"/><path d="M6 4l3 3-3 3" fill="none" stroke="#fff" stroke-width="1.5"/></svg>Leichtbau</li>
    <li><svg viewBox="0 0 14 14"><circle cx="7" cy="7" r="6" fill="none" stroke="#fff" stroke-width="1.3"/><path d="M6 4l3 3-3 3" fill="none" stroke="#fff" stroke-width="1.5"/></svg>Stahlbau</li>
    <li><svg viewBox="0 0 14 14"><circle cx="7" cy="7" r="6" fill="none" stroke="#fff" stroke-width="1.3"/><path d="M6 4l3 3-3 3" fill="none" stroke="#fff" stroke-width="1.5"/></svg>Fahrgeschäfte</li>
    <li><svg viewBox="0 0 14 14"><circle cx="7" cy="7" r="6" fill="none" stroke="#fff" stroke-width="1.3"/><path d="M6 4l3 3-3 3" fill="none" stroke="#fff" stroke-width="1.5"/></svg>und vieles mehr</li>
  </ul>

  <div class="gallery">
    <div class="gallery-photo stage" role="img" aria-label="Foto: Gerüst- und Bühnenkonstruktion im Stadion"></div>
    <div class="gallery-photo light" role="img" aria-label="Foto: Traversen mit Scheinwerfern bei einem Konzert"></div>
    <div class="gallery-photo outdoor" role="img" aria-label="Foto: Open-Air-Bühne im Aufbau"></div>
  </div>

  <footer class="contact-bar">
    <span><svg viewBox="0 0 14 14"><g fill="none" stroke="#fff" stroke-width="1.2"><circle cx="7" cy="7" r="6"/><ellipse cx="7" cy="7" rx="2.6" ry="6"/><path d="M1 7h12M2 4h10M2 10h10"/></g></svg>belsokar.de</span>
    <span><svg viewBox="0 0 14 14"><circle cx="7" cy="7" r="6.5" fill="#fff"/><path d="M3.5 5h7v4.5h-7z M3.5 5l3.5 2.6 3.5-2.6" fill="none" stroke="var(--petrol)" stroke-width="1"/></svg>info@belsokar.de</span>
  </footer>
</main>
</body>
</html>
```